Redesign Video/PIcture Check in Page

Redesign our current TetherWatchApp iPhone App checkin screens - Keep the design simple so that programmers do not have to do too much extra work to make your design work. - Look at the attached website screenshot for the overall look and feel, and color scheme - Convert the attached vector logo to iOS Icon format. - Deliver all graphics in the density required for iPhone XS Max. I will upload current check in pages that need to be reimagined. Check in needs to be more intutitive. Would like to add some gamification to the verification screen where they currently are required to enter series of random numbers. simple card game etc might work better. See TetherWatchapp in itunes and google play store. also visit quorvant-link.example or tetherwatchapp.example for more information about our company.
The Current Checkin Process:
A. Client receives alert to checkin or submits voluntary checkin
B. Clicks checkin button on home Screen.
Redesign from here:
C. Clicks on a check in from check in list screen(new screen)
D. Enters verification number(gamification something better than random numbers)
E. Opens Camera
D. Takes Selfie
F. submits photo
G. clicks check in
SEE CURRENT STEPS PIC I UPLOADED

Target Market(s)

Courts,Probation and parole,Attorneys,Sheriffs,Jails, Alternative sentencing

Colors
3277b5

Requirements
Must have
• Must be easy to navigate,Intuitive!
Nice to have
• Gamification of check in verification.
• Step by step process with next button or similar

```html
<!DOCTYPE html>
<html lang="en">
<head>
<meta charset="utf-8">
<title>TetherWatch App – Check-in Screens</title>
<link href="https://fonts.googleapis.com/css2?family=Inter:wght@200;300;400;600;700&family=Libre+Baskerville:wght@400;700&display=swap" rel="stylesheet">
<style>
:root{
  --bg:#e8ecf0;
  --frame:#f7f9fb;
  --screen:#e2eaf4;
  --navy:#0d2d6b;
  --navy-2:#1a3c84;
  --sky:#6a9bd6;
  --ink:#3b4352;
  --muted:#8b94a3;
  --line:#c9d3e0;
  --alert:#e8332f;
  --btn-grey:#b9c1cc;
}
*{box-sizing:border-box;margin:0;padding:0}
html,body{width:1200px;height:1109px;overflow:hidden;background:var(--bg);font-family:"Inter",Helvetica,Arial,sans-serif;color:var(--ink)}
.canvas{position:relative;width:1200px;height:1109px}

.intro{position:absolute;left:40px;top:40px;width:275px}
.brand{display:flex;align-items:center;gap:14px;margin-bottom:34px}
.brand-dot{width:70px;height:70px;border-radius:50%;background:var(--navy)}
.brand-name{font-size:20px;font-weight:600;color:var(--navy)}
.intro h1{font-family:"Libre Baskerville",Georgia,serif;font-weight:400;font-size:20px;letter-spacing:.5px;color:#3d4350;margin-bottom:10px;white-space:nowrap}
.intro p{font-size:9.5px;line-height:1.55;color:#5b6270}

.phone{position:absolute;width:250px;height:500px;background:var(--frame);border-radius:38px;padding:8px;box-shadow:0 18px 34px rgba(40,60,90,.16)}
.screen{position:relative;width:100%;height:100%;border-radius:31px;background:var(--screen);overflow:hidden}
.notch{position:absolute;top:0;left:50%;transform:translateX(-50%);width:120px;height:20px;background:var(--frame);border-radius:0 0 14px 14px;z-index:5}

.menu{position:absolute;left:18px;top:36px;width:16px}
.menu i{display:block;height:2px;background:var(--navy);margin-bottom:3px}
.user{position:absolute;right:16px;top:34px;display:flex;align-items:center;gap:6px;font-size:8px;font-weight:600}
.avatar{width:26px;height:26px;border-radius:50%;background:radial-gradient(circle at 50% 40%,#9b8a7a,#4a4038);border:2px solid #fff}
.title{position:absolute;left:18px;top:62px;font-size:28px;font-weight:200;color:var(--navy-2)}
.req{position:absolute;left:18px;top:104px}
.req b{display:block;font-size:10.5px;font-weight:600}
.req span{font-size:8px;color:var(--muted)}

.tabs{position:absolute;left:0;right:0;bottom:0;height:56px;border-top:1px solid var(--line);display:flex;justify-content:space-around;align-items:center;padding-bottom:6px;background:var(--screen)}
.tab{display:flex;flex-direction:column;align-items:center;gap:3px;font-size:7px;color:var(--muted)}
.tab.active{color:var(--navy);font-weight:600}
.tab svg{width:16px;height:16px;stroke:currentColor;fill:none;stroke-width:1.5}

/* home */
.home{background:var(--sky)}
.home .title,.home .user{color:#fff}
.home .title{top:50px}
.orb{position:absolute;border-radius:50%;background:var(--navy-2);display:flex;align-items:center;justify-content:center;box-shadow:0 6px 14px rgba(10,30,80,.3)}
.orb svg{stroke:#fff;fill:none;stroke-width:2}
.orb-label{position:absolute;font-size:8px;color:#fff;text-align:center;width:70px}

/* camera */
.camera .photo{position:absolute;inset:0;background:linear-gradient(160deg,#6b6a68 0%,#3e3d3c 55%,#232323 100%)}
.cancel{position:absolute;left:20px;bottom:62px;color:#fff;font-size:12px;font-weight:600}
.shutter{position:absolute;left:50%;bottom:40px;transform:translateX(-50%);width:58px;height:58px;border-radius:50%;background:#fff;box-shadow:0 0 0 4px rgba(255,255,255,.4)}
.flip{position:absolute;right:22px;bottom:56px;stroke:#fff;fill:none;stroke-width:1.5}

/* list */
.list{position:absolute;left:18px;right:16px;top:100px}
.row{display:flex;justify-content:space-between;align-items:center;height:38px}
.row b{display:block;font-size:10px;font-weight:600}
.row span{font-size:7.5px;color:var(--muted)}
.tick{width:18px;height:18px;border-radius:50%;background:var(--navy);display:flex;align-items:center;justify-content:center;flex:none}
.tick svg{stroke:#fff;fill:none;stroke-width:2}
.pin svg{stroke:var(--ink);fill:none;stroke-width:1.4}

/* keypad */
.digits{position:absolute;left:22px;top:140px;display:flex;gap:22px;font-size:20px;font-weight:200;color:var(--navy-2)}
.digits em{font-style:normal;display:inline-block;width:16px;border-bottom:1px solid var(--muted);height:26px}
.pad{position:absolute;left:29px;top:176px;width:176px;height:176px}
.key{position:absolute;width:36px;height:36px;border-radius:50%;background:var(--navy);display:flex;align-items:center;justify-content:center;font-size:15px;font-weight:200;color:var(--navy)}
.key.lit{background:#fff}
.submit{position:absolute;left:24px;right:24px;bottom:72px;height:32px;border-radius:16px;background:var(--btn-grey);color:#fff;font-size:10px;font-weight:600;display:flex;align-items:center;justify-content:center}

/* courts */
.courts{position:absolute;left:18px;right:16px;top:104px}
.court{height:38px;border-bottom:1px solid var(--line);display:flex;justify-content:space-between;align-items:center}
.court b{display:block;font-size:9px;font-weight:600;color:var(--alert);line-height:1.3}
.court span{font-size:6.5px;color:var(--muted)}
.court .tick{width:16px;height:16px}

/* selfie */
.selfie{position:absolute;left:50%;top:200px;transform:translateX(-50%);width:130px;height:130px;border-radius:28px;background:radial-gradient(circle at 55% 40%,#8c7b6c,#3f3630 75%)}
.fab{position:absolute;left:50%;bottom:76px;transform:translateX(-50%);width:56px;height:56px;border-radius:50%;background:#fff;display:flex;flex-direction:column;align-items:center;justify-content:center;font-size:6.5px;color:var(--navy);box-shadow:0 6px 14px rgba(40,60,90,.18)}
.fab svg{stroke:var(--navy);fill:none;stroke-width:1.5}

/* done */
.done{background:radial-gradient(circle at 50% 46%,#f4f7fb 0%,var(--screen) 65%)}
.done-title{position:absolute;top:120px;width:100%;text-align:center;color:var(--navy);font-size:20px;line-height:1.1}
.done-title b{font-weight:700;display:block}
.done-title span{font-weight:300}
.done-badge{position:absolute;left:50%;top:190px;transform:translateX(-50%);width:88px;height:88px;border-radius:50%;background:var(--navy);border:5px solid #fff;display:flex;align-items:center;justify-content:center}
.done-badge svg{stroke:#fff;fill:none;stroke-width:6}
.done-note{position:absolute;top:300px;width:100%;text-align:center;font-size:8px;color:var(--ink)}
.done-btn{position:absolute;left:50%;top:325px;transform:translateX(-50%);width:110px;height:28px;border-radius:14px;background:var(--navy);color:#fff;font-size:9px;font-weight:600;display:flex;align-items:center;justify-content:center}
</style>
</head>
<body>
<div class="canvas">

  <section class="intro">
    <div class="brand"><div class="brand-dot"></div><div class="brand-name">TetherWatch</div></div>
    <h1>TETHERWATCH APP</h1>
    <p>The patent pending Quorvant TETHERWATCH APP for smartphones is an alternative to ankle-bracelet monitoring. It allows intense monitoring while it tracks and records the movements of low-risk, non-violent offenders with advanced features including: GPS Tracking, Biometric Identification, and Dynamic Remote Check-ins.</p>
  </section>

  <!-- Home -->
  <div class="phone" style="left:330px;top:40px">
    <div class="screen home">
      <div class="notch"></div>
      <div class="user">Marcus D Fenley <div class="avatar" role="img" aria-label="User portrait"></div></div>
      <div class="title">Check in</div>
      <div class="orb" style="left:134px;top:120px;width:54px;height:54px"><svg width="20" height="22" viewBox="0 0 20 22"><path d="M10 20s7-7 7-12a7 7 0 0 0-14 0c0 5 7 12 7 12z"/><circle cx="10" cy="8" r="2.5"/></svg></div>
      <div class="orb-label" style="left:126px;top:178px">Map</div>
      <div class="orb" style="left:34px;top:170px;width:54px;height:54px"><svg width="22" height="14" viewBox="0 0 22 14"><path d="M1 12l6-8 4 6 4-5 6 7"/></svg></div>
      <div class="orb-label" style="left:26px;top:228px">Stats</div>
      <div class="orb" style="left:166px;top:196px;width:54px;height:54px"><svg width="24" height="16" viewBox="0 0 24 16" style="stroke:var(--alert)"><rect x="2" y="4" width="20" height="8" rx="4"/></svg></div>
      <div class="orb-label" style="left:158px;top:254px">Bracelet</div>
      <div class="orb" style="left:78px;top:250px;width:94px;height:94px;background:var(--navy)"><svg width="34" height="38" viewBox="0 0 20 22"><path d="M10 20s7-7 7-12a7 7 0 0 0-14 0c0 5 7 12 7 12z"/><circle cx="10" cy="8" r="2.5"/></svg></div>
      <div class="orb" style="left:24px;top:330px;width:54px;height:54px"><svg width="8" height="20" viewBox="0 0 8 20"><path d="M4 2v1M4 8v10"/></svg></div>
      <div class="orb-label" style="left:16px;top:388px">Information</div>
    </div>
  </div>

  <!-- Camera -->
  <div class="phone" style="left:620px;top:40px">
    <div class="screen camera">
      <div class="photo" role="img" aria-label="Live camera view of the user taking a selfie"></div>
      <div class="notch"></div>
      <div class="cancel">Cancel</div>
      <div class="shutter"></div>
      <svg class="flip" width="22" height="18" viewBox="0 0 22 18"><rect x="1" y="4" width="20" height="13" rx="2"/><circle cx="11" cy="10.5" r="3.5"/><path d="M7 4l2-3h4l2 3"/></svg>
    </div>
  </div>

  <!-- Court dates -->
  <div class="phone" style="left:910px;top:40px">
    <div class="screen">
      <div class="notch"></div>
      <div class="menu"><i></i><i></i><i></i></div>
      <div class="user">Marcus D Fenley <div class="avatar" role="img" aria-label="User portrait"></div></div>
      <div class="title">Court Dates</div>
      <div class="courts">
        <div class="court"><div><b>Friday, Oct 12th at 9:00 a.m.</b><span>Harlow County Circuit Court Room 105</span></div><svg width="16" height="12" viewBox="0 0 16 12" fill="none" stroke="#3b4352" stroke-width="1.3"><rect x="1" y="2" width="10" height="8"/><path d="M11 5l4-2v6l-4-2"/></svg></div>
        <div class="court"><div><b>Thursday, Sep 3rd at 1:00 p.m.</b><span>Ridgefield District Court</span></div><div class="tick"><svg width="9" height="7" viewBox="0 0 10 8"><path d="M1 4l3 3 5-6"/></svg></div></div>
        <div class="court"><div><b>Thursday, Aug 8th at 2:00 p.m.</b><span>Ridgefield District Court</span></div><svg width="16" height="12" viewBox="0 0 16 12" fill="none" stroke="#3b4352" stroke-width="1.3"><rect x="1" y="2" width="10" height="8"/><path d="M11 5l4-2v6l-4-2"/></svg></div>
        <div class="court"><div><b>Thursday, Jul 4th at 1:00 p.m.</b><span>Ridgefield District Court</span></div><div class="tick"><svg width="9" height="7" viewBox="0 0 10 8"><path d="M1 4l3 3 5-6"/></svg></div></div>
        <div class="court"><div><b>Thursday, Jun 6th at 3:00 p.m.</b><span>Ridgefield District Court</span></div><div class="tick"><svg width="9" height="7" viewBox="0 0 10 8"><path d="M1 4l3 3 5-6"/></svg></div></div>
        <div class="court"><div><b>Thursday, Apr 2nd at 2:00 p.m.</b><span>Ridgefield District Court</span></div><div class="tick"><svg width="9" height="7" viewBox="0 0 10 8"><path d="M1 4l3 3 5-6"/></svg></div></div>
        <div class="court"><div><b>Thursday, Mar 3rd at 1:00 p.m.</b><span>Ridgefield District Court</span></div><div class="tick"><svg width="9" height="7" viewBox="0 0 10 8"><path d="M1 4l3 3 5-6"/></svg></div></div>
        <div class="court"><div><b>Thursday, Feb 5th at 1:00 p.m.</b><span>Ridgefield District Court</span></div><svg width="16" height="12" viewBox="0 0 16 12" fill="none" stroke="#3b4352" stroke-width="1.3"><rect x="1" y="2" width="10" height="8"/><path d="M11 5l4-2v6l-4-2"/></svg></div>
      </div>
      <nav class="tabs">
        <div class="tab"><svg viewBox="0 0 16 16"><path d="M2 8l6-5 6 5v6H2z"/></svg>Home</div>
        <div class="tab active"><svg viewBox="0 0 16 16"><path d="M8 15s5-5 5-9a5 5 0 0 0-10 0c0 4 5 9 5 9z"/><circle cx="8" cy="6" r="1.8"/></svg>Check-ins</div>
        <div class="tab"><svg viewBox="0 0 16 16"><path d="M1 3l4.5-1.5 5 1.5L15 1.5v11.5l-4.5 1.5-5-1.5L1 14.5zM5.5 1.5v11.5M10.5 3v11.5"/></svg>Map</div>
        <div class="tab"><svg viewBox="0 0 16 16"><circle cx="8" cy="8" r="6.5"/><path d="M8 7v4M8 5v.5"/></svg>Info</div>
      </nav>
    </div>
  </div>

  <!-- Check-ins list -->
  <div class="phone" style="left:40px;top:590px">
    <div class="screen">
      <div class="notch"></div>
      <div class="menu"><i></i><i></i><i></i></div>
      <div class="user">Marcus D Fenley <div class="avatar" role="img" aria-label="User portrait"></div></div>
      <div class="title">Check ins</div>
      <div class="list">
        <div class="row"><div><b>Voluntary Check-in Request</b><span>20 Oct 2018 10:27:59</span></div><div class="pin"><svg width="14" height="16" viewBox="0 0 14 16"><path d="M7 15s5-5 5-9a5 5 0 0 0-10 0c0 4 5 9 5 9z"/><circle cx="7" cy="6" r="1.8"/></svg></div></div>
        <div class="row"><div><b>Voluntary Check-in Request</b><span>20 Oct 2018 10:27:59</span></div><div class="tick"><svg width="10" height="8" viewBox="0 0 10 8"><path d="M1 4l3 3 5-6"/></svg></div></div>
        <div class="row"><div><b>Voluntary Check-in Request</b><span>20 Oct 2018 10:27:59</span></div><div class="pin"><svg width="14" height="16" viewBox="0 0 14 16"><path d="M7 15s5-5 5-9a5 5 0 0 0-10 0c0 4 5 9 5 9z"/><circle cx="7" cy="6" r="1.8"/></svg></div></div>
        <div class="row"><div><b>Voluntary Check-in Request</b><span>20 Oct 2018 10:27:59</span></div><div class="tick"><svg width="10" height="8" viewBox="0 0 10 8"><path d="M1 4l3 3 5-6"/></svg></div></div>
        <div class="row"><div><b>Voluntary Check-in Request</b><span>20 Oct 2018 10:27:59</span></div><div class="tick"><svg width="10" height="8" viewBox="0 0 10 8"><path d="M1 4l3 3 5-6"/></svg></div></div>
        <div class="row"><div><b>Voluntary Check-in Request</b><span>20 Oct 2018 10:27:59</span></div><div class="tick"><svg width="10" height="8" viewBox="0 0 10 8"><path d="M1 4l3 3 5-6"/></svg></div></div>
        <div class="row"><div><b>Voluntary Check-in Request</b><span>20 Oct 2018 10:27:59</span></div><div class="tick"><svg width="10" height="8" viewBox="0 0 10 8"><path d="M1 4l3 3 5-6"/></svg></div></div>
        <div class="row"><div><b>Voluntary Check-in Request</b><span>20 Oct 2018 10:27:59</span></div><div class="pin"><svg width="14" height="16" viewBox="0 0 14 16"><path d="M7 15s5-5 5-9a5 5 0 0 0-10 0c0 4 5 9 5 9z"/><circle cx="7" cy="6" r="1.8"/></svg></div></div>
      </div>
      <nav class="tabs">
        <div class="tab"><svg viewBox="0 0 16 16"><path d="M2 8l6-5 6 5v6H2z"/></svg>Home</div>
        <div class="tab active"><svg viewBox="0 0 16 16"><path d="M8 15s5-5 5-9a5 5 0 0 0-10 0c0 4 5 9 5 9z"/><circle cx="8" cy="6" r="1.8"/></svg>Check-ins</div>
        <div class="tab"><svg viewBox="0 0 16 16"><path d="M1 3l4.5-1.5 5 1.5L15 1.5v11.5l-4.5 1.5-5-1.5L1 14.5zM5.5 1.5v11.5M10.5 3v11.5"/></svg>Map</div>
        <div class="tab"><svg viewBox="0 0 16 16"><circle cx="8" cy="8" r="6.5"/><path d="M8 7v4M8 5v.5"/></svg>Info</div>
      </nav>
    </div>
  </div>

  <!-- Verification pad -->
  <div class="phone" style="left:330px;top:590px">
    <div class="screen">
      <div class="notch"></div>
      <div class="menu"><i></i><i></i><i></i></div>
      <div class="user">Marcus D Fenley <div class="avatar" role="img" aria-label="User portrait"></div></div>
      <div class="title">Check in</div>
      <div class="req"><b>Voluntary Check-in Request</b><span>20 Oct 2018 10:27:59</span></div>
      <div class="digits"><span>9</span><span>8</span><em></em><em></em></div>
      <div class="pad">
        <div class="key" style="left:56px;top:0"></div>
        <div class="key" style="left:28px;top:28px"></div>
        <div class="key lit" style="left:84px;top:28px">9</div>
        <div class="key" style="left:0;top:56px"></div>
        <div class="key" style="left:56px;top:56px"></div>
        <div class="key" style="left:112px;top:56px"></div>
        <div class="key" style="left:28px;top:84px"></div>
        <div class="key lit" style="left:84px;top:84px">8</div>
        <div class="key" style="left:140px;top:84px"></div>
        <div class="key" style="left:56px;top:112px"></div>
        <div class="key" style="left:112px;top:112px"></div>
        <div class="key" style="left:84px;top:140px"></div>
      </div>
      <div class="submit">Submit</div>
      <nav class="tabs">
        <div class="tab"><svg viewBox="0 0 16 16"><path d="M2 8l6-5 6 5v6H2z"/></svg>Home</div>
        <div class="tab active"><svg viewBox="0 0 16 16"><path d="M8 15s5-5 5-9a5 5 0 0 0-10 0c0 4 5 9 5 9z"/><circle cx="8" cy="6" r="1.8"/></svg>Check-ins</div>
        <div class="tab"><svg viewBox="0 0 16 16"><path d="M1 3l4.5-1.5 5 1.5L15 1.5v11.5l-4.5 1.5-5-1.5L1 14.5zM5.5 1.5v11.5M10.5 3v11.5"/></svg>Map</div>
        <div class="tab"><svg viewBox="0 0 16 16"><circle cx="8" cy="8" r="6.5"/><path d="M8 7v4M8 5v.5"/></svg>Info</div>
      </nav>
    </div>
  </div>

  <!-- Selfie review -->
  <div class="phone" style="left:620px;top:590px">
    <div class="screen">
      <div class="notch"></div>
      <div class="menu"><i></i><i></i><i></i></div>
      <div class="user">Marcus D Fenley <div class="avatar" role="img" aria-label="User portrait"></div></div>
      <div class="title">Check in</div>
      <div class="req"><b>Voluntary Check-in Request</b><span>20 Oct 2018 10:27:59</span></div>
      <div class="digits"><span>9</span><span>8</span><span>K</span><span>G</span></div>
      <div class="selfie" role="img" aria-label="Captured selfie of the user"></div>
      <div class="fab"><svg width="14" height="16" viewBox="0 0 14 16"><path d="M7 15s5-5 5-9a5 5 0 0 0-10 0c0 4 5 9 5 9z"/><circle cx="7" cy="6" r="1.8"/></svg>Check-ins</div>
      <nav class="tabs">
        <div class="tab"><svg viewBox="0 0 16 16"><path d="M2 8l6-5 6 5v6H2z"/></svg>Home</div>
        <div class="tab active"><svg viewBox="0 0 16 16"><path d="M8 15s5-5 5-9a5 5 0 0 0-10 0c0 4 5 9 5 9z"/><circle cx="8" cy="6" r="1.8"/></svg>Check-ins</div>
        <div class="tab"><svg viewBox="0 0 16 16"><path d="M1 3l4.5-1.5 5 1.5L15 1.5v11.5l-4.5 1.5-5-1.5L1 14.5zM5.5 1.5v11.5M10.5 3v11.5"/></svg>Map</div>
        <div class="tab"><svg viewBox="0 0 16 16"><circle cx="8" cy="8" r="6.5"/><path d="M8 7v4M8 5v.5"/></svg>Info</div>
      </nav>
    </div>
  </div>

  <!-- Completed -->
  <div class="phone" style="left:910px;top:590px">
    <div class="screen done">
      <div class="notch"></div>
      <div class="done-title"><b>Check in</b><span>Completed</span></div>
      <div class="done-badge"><svg width="44" height="34" viewBox="0 0 44 34"><path d="M4 18l12 12L40 4"/></svg></div>
      <div class="done-note">Check-in successfully complete.</div>
      <div class="done-btn">Done</div>
      <nav class="tabs">
        <div class="tab"><svg viewBox="0 0 16 16"><path d="M2 8l6-5 6 5v6H2z"/></svg>Home</div>
        <div class="tab active"><svg viewBox="0 0 16 16"><path d="M8 15s5-5 5-9a5 5 0 0 0-10 0c0 4 5 9 5 9z"/><circle cx="8" cy="6" r="1.8"/></svg>Check-ins</div>
        <div class="tab"><svg viewBox="0 0 16 16"><path d="M1 3l4.5-1.5 5 1.5L15 1.5v11.5l-4.5 1.5-5-1.5L1 14.5zM5.5 1.5v11.5M10.5 3v11.5"/></svg>Map</div>
        <div class="tab"><svg viewBox="0 0 16 16"><circle cx="8" cy="8" r="6.5"/><path d="M8 7v4M8 5v.5"/></svg>Info</div>
      </nav>
    </div>
  </div>

</div>
</body>
</html>
```